2023 GLR Festival Form

• We are looking for a one-page form front and back. Something that comes that way, and we don’t have to merge it.
• Must be a fillable form, PDF version.
• The form will need to be editable; we will make minor changes as needed to the form, mainly contact information.
• Please add pictures, descriptions, and a registration area that includes a grand total donated.
• Attached are descriptions, links, and additional information that may help you develop a fluid registration form for us.

```html
<!DOCTYPE html>
<html lang="en">
<head>
<meta charset="utf-8">
<title>25th Annual GLR Festival – Registration Form</title>
<link href="https://fonts.googleapis.com/css2?family=Poppins:wght@400;500;600;700&family=Oswald:wght@600&display=swap" rel="stylesheet">
<style>
:root{
  --bg:#e1e1e1;
  --paper:#ffffff;
  --blue:#2e3192;
  --navy:#23266e;
  --ink:#1b1b1b;
  --grey:#a6a6a7;
  --grey-dark:#949495;
  --line:#2e3192;
}
*{box-sizing:border-box;margin:0;padding:0}
html,body{width:1200px;height:1200px;overflow:hidden;background:var(--bg);font-family:'Poppins',sans-serif;color:var(--ink)}
.sheet{position:absolute;top:320px;width:506px;height:655px;background:var(--paper);overflow:hidden}
.sheet--front{left:68px}
.sheet--back{left:630px}
.abs{position:absolute;white-space:nowrap}
.header{position:absolute;left:0;top:0;width:506px;height:120px}
.brand{position:absolute;left:14px;top:40px;width:92px;font-size:10px;font-weight:600;line-height:1.15;color:var(--ink);white-space:normal}
.brand-dot{display:inline-block;width:9px;height:9px;border-radius:50%;background:var(--ink);margin-bottom:4px}
.edition{position:absolute;left:128px;top:18px;font-family:'Oswald',sans-serif;font-weight:600;font-size:36px;color:#fff;line-height:1}
.edition sup{font-size:17px;vertical-align:top;position:relative;top:2px}
.title{position:absolute;left:202px;top:33px;font-weight:700;font-size:23.5px;color:#fff;letter-spacing:.2px;line-height:1}
.dates{position:absolute;left:141px;top:72px;font-size:17px;font-weight:700;color:#fff;line-height:1}
.dates sup{font-size:9px;vertical-align:top}
.dates .thin{font-weight:500}
.divider{position:absolute;left:344px;top:71px;width:1px;height:28px;background:#fff}
.venue{position:absolute;left:352px;top:70px;font-size:11.5px;color:#fff;line-height:1.2;display:flex;gap:4px}
.venue svg{margin-top:2px}
.label{font-size:7.2px;font-weight:500;color:var(--blue)}
.heading{font-size:7.2px;font-weight:600;color:var(--blue)}
.small{font-size:6.3px;color:var(--ink)}
.bold{font-weight:600}
.field{position:absolute;height:17px;border:1px solid var(--line);background:#fff}
.opts{font-size:6.3px;line-height:1}
.check{display:inline-block;width:7px;height:7px;border:1px solid #bbb;vertical-align:-1px;margin-right:4px}
.opt{margin-right:8px}
.tier{position:absolute;left:34px;width:116px;height:12px;font-size:7px;padding-left:6px;line-height:12px}
.tier-box{position:absolute;left:21px;width:6px;height:6px;border:1px solid #ccc}
.amount{position:absolute;left:163px;width:53px;height:17px;border:1px solid var(--line);font-size:7px;font-weight:600;display:flex;align-items:center;padding-left:13px}
.diamond{background:linear-gradient(90deg,#9c9c9c,#e6e6e6)}
.gold{background:linear-gradient(90deg,#c59a2f,#f4e08d 60%,#c99e3a)}
.silver{background:linear-gradient(90deg,#c4c4c4,#f4f4f4)}
.bronze{background:linear-gradient(90deg,#cf8f5c,#f2c49c)}
.friend{background:var(--blue);color:#fff}
.contact-box{position:absolute;height:17px;border:1px solid var(--line);font-size:7px;display:flex;align-items:center;gap:5px;padding-left:8px;white-space:nowrap;overflow:hidden}
.bar{position:absolute;background:var(--blue);color:#fff;font-size:7.2px;display:flex;align-items:center}
.agenda-table{position:absolute;left:23px;top:518px;width:230px;border-collapse:collapse;font-size:7.2px;color:#fff}
.agenda-table td{height:17.9px;padding-left:8px;vertical-align:middle}
.agenda-table tr:first-child td{height:21px;padding-top:6px}
.agenda-table .time{width:77px;background:var(--blue)}
.agenda-table tr:nth-child(even) .time{background:var(--navy)}
.agenda-table .what{background:var(--grey)}
.agenda-table tr:nth-child(even) .what{background:var(--grey-dark)}
.hotel{position:absolute;left:280px;top:518px;width:199px;height:103px}
.hotel-top{height:37px;background:var(--grey);color:#fff;font-size:6px;font-weight:600;padding:6px 8px;line-height:1.3}
.hotel-bottom{height:66px;background:var(--blue);color:#fff;font-size:5.2px;padding:6px 8px;line-height:1.25;white-space:nowrap;overflow:hidden}
.tick{display:inline-block;width:5px;height:5px;border-radius:50%;background:currentColor;margin-right:4px;vertical-align:0}
.blue-tick{display:inline-block;width:5px;height:5px;border-radius:50%;background:var(--blue);margin-right:4px;vertical-align:0}
.foot{position:absolute;left:0;bottom:0;width:506px;height:7px;background:#000}
.price{font-size:11px;font-weight:500}
.price b{color:var(--blue);font-weight:500}
.spa-bar{position:absolute;left:25px;top:333px;width:178px;height:24px;display:flex;font-size:6px;color:#fff;font-weight:600}
.spa-bar .url{background:var(--blue);width:110px;display:flex;align-items:center;padding-left:7px;clip-path:polygon(0 0,100% 0,92% 100%,0 100%)}
.spa-bar .hours{background:#8f8f90;flex:1;display:flex;align-items:center;justify-content:flex-end;padding-right:6px;margin-left:-9px}
.photo{position:absolute;left:25px;top:534px;width:180px;height:99px;background:radial-gradient(ellipse at 50% 45%,#f7d64a 0,#f3cd3a 35%,#fbf3d0 62%,#ffffff 80%)}
.sponsor-box{position:absolute;left:232px;top:335px;width:247px;height:77px;border:1px solid var(--line)}
.sponsor-row{position:absolute;left:8px;font-size:7px;font-weight:500;white-space:nowrap}
.sponsor-row b{color:var(--blue);font-weight:500}
.partner{position:absolute;font-size:9px;font-weight:700;color:var(--ink)}
.partner-small{position:absolute;font-size:5.5px;font-weight:700;color:var(--ink);white-space:nowrap}
.meeting-sponsors{position:absolute;left:232px;top:606px;width:248px;display:flex;justify-content:space-between;align-items:center;font-size:10px;font-weight:700;color:var(--ink)}
</style>
</head>
<body>

<section class="sheet sheet--front">
  <svg class="header" viewBox="0 0 506 120" width="506" height="120">
    <polygon points="107,0 506,0 506,110 107,110 125,55" fill="#2e3192"/>
    <rect x="0" y="109" width="506" height="2" fill="#2e3192"/>
    <rect x="0" y="114" width="506" height="5" fill="#000"/>
    <polygon points="119,21 210,21 198,68 110,68" fill="#111"/>
  </svg>
  <div class="brand"><span class="brand-dot"></span><br>Lakeland Growers Federation</div>
  <div class="edition">25<sup>TH</sup></div>
  <div class="title">ANNUAL GLR FESTIVAL</div>
  <div class="dates">OCTOBER 6<sup>TH</sup> <span class="thin">AND</span> 7<sup>TH</sup></div>
  <div class="divider"></div>
  <div class="venue"><svg width="9" height="12" viewBox="0 0 9 12"><path d="M4.5 0C2 0 0 2 0 4.5 0 7.5 4.5 12 4.5 12S9 7.5 9 4.5C9 2 7 0 4.5 0z" fill="#fff"/><circle cx="4.5" cy="4.5" r="1.7" fill="#2e3192"/></svg><span>Lexington, KY at the<br>Harbor Oak Resort</span></div>

  <div class="abs bold" style="left:0;width:506px;text-align:center;top:129px;font-size:13px">REGISTRATION FORM INFORMATION</div>

  <div class="abs label" style="left:23px;top:159px">Name of company</div>
  <div class="field" style="left:163px;top:156px;width:315px"></div>
  <div class="abs label" style="left:23px;top:188px">Name of the contact person</div>
  <div class="field" style="left:163px;top:185px;width:315px"></div>
  <div class="abs label" style="left:23px;top:217px">Are you attending?</div>
  <div class="abs opts" style="left:163px;top:218px"><span class="opt"><span class="check"></span>Will not be attending</span><span class="opt"><span class="check"></span>Donation only</span><span class="opt"><span class="check"></span>Donation for</span></div>
  <div class="abs label" style="left:23px;top:247px">Names of those who are attending</div>
  <div class="field" style="left:163px;top:244px;width:111px"></div>
  <div class="field" style="left:280px;top:244px;width:85px"></div>
  <div class="field" style="left:371px;top:244px;width:107px"></div>
  <div class="abs label" style="left:23px;top:278px">Email address of the contact person</div>
  <div class="field" style="left:163px;top:275px;width:315px"></div>
  <div class="abs opts" style="left:163px;top:299px"><span class="opt"><span class="check"></span>Golf</span><span class="opt"><span class="check"></span>Spa</span><span class="opt"><span class="check"></span>Stonebridge</span><span class="opt"><span class="check"></span>Sporting Clay</span><span class="opt"><span class="check"></span>Banquet</span></div>

  <div class="abs heading" style="left:23px;top:317px">SPONSORSHIPS LEVELS</div>
  <span class="tier-box" style="top:339px"></span><div class="tier diamond" style="top:334px">Diamond Sponsor</div><div class="amount" style="top:331px">$5,000</div>
  <span class="tier-box" style="top:362px"></span><div class="tier gold" style="top:357px">Golden Egg Sponsor</div><div class="amount" style="top:354px">$3,000</div>
  <span class="tier-box" style="top:385px"></span><div class="tier silver" style="top:380px">Silver Chicken Sponsor</div><div class="amount" style="top:377px">$2,000</div>
  <span class="tier-box" style="top:408px"></span><div class="tier bronze" style="top:403px">Bronze Turkey Sponsor</div><div class="amount" style="top:401px">$1,000</div>
  <span class="tier-box" style="top:430px"></span><div class="tier friend" style="top:425px">Friend of GLR</div><div class="amount" style="top:422px">$500</div>
  <div class="abs small" style="left:23px;top:445px;line-height:1.25">The GLR is a nonprofit organization, and your donations<br>are tax-deductible.</div>

  <div class="abs bold" style="left:280px;top:323px;font-size:7.2px">QUESTIONS Contact Dana Whitlow at</div>
  <div class="contact-box" style="left:280px;top:339px;width:86px"><svg width="8" height="8" viewBox="0 0 8 8"><path d="M1.5 0 3 2 2.2 3.1c.6 1.2 1.5 2.1 2.7 2.7L6 5l2 1.5-1 1.4C3.6 7.8.2 4.4 0 1z" fill="#2e3192"/></svg>555-404-0142</div>
  <div class="contact-box" style="left:371px;top:339px;width:107px;padding-left:6px"><svg width="9" height="7" viewBox="0 0 9 7"><rect width="9" height="7" fill="#2e3192"/><path d="M0 0l4.5 4L9 0" stroke="#fff" stroke-width=".8" fill="none"/></svg>dwhitlow@lgfed.org</div>
  <div class="abs bold" style="left:280px;top:367px;font-size:7px;line-height:1.2">Deadline for<br>Registration</div>
  <div class="abs" style="left:337px;top:368px;width:1px;height:17px;background:#000"></div>
  <div class="abs bold" style="left:345px;top:367px;font-size:12px;color:var(--blue)">SEPTEMBER 15, <span style="color:#111">2022</span></div>
  <div class="contact-box" style="left:280px;top:390px;width:199px;height:20px;font-size:5.2px;line-height:1.2;align-items:center"><span class="check" style="width:6px;height:6px"></span><span>Make checks payable to the Lakeland Growers Federation<br>or pay via credit card using the Registration form.</span></div>
  <div class="abs bold" style="left:280px;top:426px;font-size:7px;line-height:1.2">Email Registration<br>Forms to</div>
  <div class="contact-box" style="left:356px;top:424px;width:122px;padding-left:10px"><svg width="9" height="7" viewBox="0 0 9 7"><rect width="9" height="7" fill="#2e3192"/><path d="M0 0l4.5 4L9 0" stroke="#fff" stroke-width=".8" fill="none"/></svg>dwhitlow@lgfed.org</div>

  <div class="bar" style="left:23px;top:462px;width:255px;height:17px;padding-left:8px">Mail payment and this registration</div>
  <div class="contact-box" style="left:280px;top:462px;width:199px"><svg width="7" height="9" viewBox="0 0 9 12"><path d="M4.5 0C2 0 0 2 0 4.5 0 7.5 4.5 12 4.5 12S9 7.5 9 4.5C9 2 7 0 4.5 0z" fill="#2e3192"/><circle cx="4.5" cy="4.5" r="1.7" fill="#fff"/></svg>&nbsp;1180 College Station, Marlow, KY 42000</div>

  <div class="abs heading" style="left:23px;top:504px">AGENDA</div>
  <div class="abs heading" style="left:280px;top:504px">HOTEL INFORMATION</div>
  <table class="agenda-table">
    <tr><td class="time">1:30 PM</td><td class="what">Set up Silent Auction</td></tr>
    <tr><td class="time">4:30 PM</td><td class="what">Registration opens</td></tr>
    <tr><td class="time">5:00 PM</td><td class="what">Silent auction/music/cash bar opens</td></tr>
    <tr><td class="time">6:00 PM</td><td class="what">Annual Meeting and Awards Banquet</td></tr>
    <tr><td class="time">8:45 PM - 11:00 PM</td><td class="what">Moonlight Keys event</td></tr>
  </table>
  <div class="hotel">
    <div class="hotel-top"><span class="tick"></span>Harbor Oak Golf Resort &amp; Spa<br><span class="tick"></span>dates are October 6th and 7th in Lexington,<br>&nbsp;&nbsp;&nbsp;KY at the Harbor Oak Resort.</div>
    <div class="hotel-bottom"><b style="font-size:6px"><span class="tick"></span>Harbor Oak Reservations at<br>&nbsp;&nbsp;&nbsp;1 (800) 555-0190 or (859) 555-0100</b><br>
    &nbsp;&nbsp;&nbsp;✓ Book by September 15th to make your room reservations.<br>&nbsp;&nbsp;&nbsp;&nbsp;&nbsp;Mention Lakeland Growers or GLR for your room block.<br>
    &nbsp;&nbsp;&nbsp;✓ https://www.harboroakresort.com/stay/golf-resort-<br>&nbsp;&nbsp;&nbsp;&nbsp;&nbsp;and-spa/overview/?room-block=glr-festival</div>
  </div>
  <div class="foot"></div>
</section>

<section class="sheet sheet--back">
  <svg class="header" viewBox="0 0 506 120" width="506" height="120">
    <polygon points="107,0 506,0 506,110 107,110 125,55" fill="#2e3192"/>
    <rect x="0" y="109" width="506" height="2" fill="#2e3192"/>
    <rect x="0" y="114" width="506" height="5" fill="#000"/>
    <polygon points="119,21 210,21 198,68 110,68" fill="#111"/>
  </svg>
  <div class="brand"><span class="brand-dot"></span><br>Lakeland Growers Federation</div>
  <div class="edition">25<sup>TH</sup></div>
  <div class="title">ANNUAL GLR FESTIVAL</div>
  <div class="dates">OCTOBER 6<sup>TH</sup> <span class="thin">AND</span> 7<sup>TH</sup></div>
  <div class="divider"></div>
  <div class="venue"><svg width="9" height="12" viewBox="0 0 9 12"><path d="M4.5 0C2 0 0 2 0 4.5 0 7.5 4.5 12 4.5 12S9 7.5 9 4.5C9 2 7 0 4.5 0z" fill="#fff"/><circle cx="4.5" cy="4.5" r="1.7" fill="#2e3192"/></svg><span>Lexington, KY at the<br>Harbor Oak Resort</span></div>

  <div class="abs heading" style="left:25px;top:131px;font-size:8px">AGENDA</div>
  <div class="abs bold" style="left:25px;top:149px;font-size:6.5px">FRIDAY</div>
  <div class="abs bold" style="left:25px;top:159px;font-size:6px">Stonebridge Tailgating</div>
  <div class="abs small" style="left:25px;top:169px;line-height:1.25">Complimentary Meal &amp; Stonebridge<br>Grandstand Reserved Seating included.</div>
  <div class="abs small" style="left:25px;top:194px">Food and fun 11:00 a.m.-1:00 p.m. EST</div>
  <div class="abs small" style="left:25px;top:210px">Races start at 1:05 p.m.</div>
  <div class="abs price" style="left:25px;top:224px">Cost per <b>person $50</b></div>
  <div class="abs bold" style="left:25px;top:248px;font-size:6px">EMAIL</div>
  <div class="field" style="left:51px;top:243px;width:153px"></div>
  <div class="abs bold" style="left:25px;top:268px;font-size:6.3px">Sponsors</div>
  <div class="abs small" style="left:25px;top:282px"><span class="blue-tick"></span>Corvane Event sponsor</div>
  <div class="abs small" style="left:25px;top:298px"><span class="blue-tick"></span>Local Beverages donated by Meadowrise</div>
  <div class="partner-small" style="left:170px;top:283px">Corvane</div>
  <div class="partner-small" style="left:170px;top:299px">Meadowrise</div>

  <div class="abs heading" style="left:25px;top:315px;font-size:8.5px">SPA</div>
  <div class="spa-bar"><div class="url">www.thespaatharboroak.com</div><div class="hours">9:30 AM- 3:30 PM ET</div></div>
  <div class="abs bold" style="left:25px;top:364px;font-size:9.5px">Limited appointments available</div>
  <div class="abs price" style="left:25px;top:378px"><b>$150.00</b> per person</div>
  <div class="abs bold" style="left:25px;top:398px;font-size:6.5px">Appointment?</div>
  <div class="abs bold" style="left:25px;top:417px;font-size:6.5px">AM</div>
  <div class="field" style="left:43px;top:412px;width:69px"></div>
  <div class="abs bold" style="left:117px;top:417px;font-size:6.5px">PM</div>
  <div class="field" style="left:132px;top:412px;width:71px"></div>

  <div class="abs heading" style="left:25px;top:440px;font-size:8.5px">BANQUET</div>
  <div class="abs bold" style="left:25px;top:453px;font-size:6px">Awards Banquet and Entertainment ticket</div>
  <div class="abs price" style="left:25px;top:462px"><b>$150</b> per person</div>
  <div class="abs bold" style="left:25px;top:481px;font-size:6px">Entertainment</div>
  <div class="abs small" style="left:25px;top:495px"><span class="blue-tick"></span>Moonlight Keys</div>
  <div class="abs small bold" style="left:25px;top:510px;line-height:1.25"><span class="blue-tick"></span>Join us for fun, games, music, and around<br>&nbsp;&nbsp;&nbsp;&nbsp;$3,000 in prizes!</div>
  <div class="photo" role="img" aria-label="Photo of three yellow chicks standing on a white background"></div>

  <div class="abs bold" style="left:231px;top:134px;font-size:6.5px">SATURDAY</div>
  <div class="abs bold" style="left:231px;top:149px;font-size:6.5px">GOLF</div>
  <div class="abs small" style="left:231px;top:160px;line-height:1.25">The scramble will be held at Harbor Oak Resort Golf Club,<br>located at 1650 Ridgeway Pike, Lexington, KY, 40500, (859) 555-0177</div>
  <div class="bar" style="left:231px;top:185px;width:248px;height:24px;justify-content:center;text-align:center;font-size:6px;line-height:1.2">https://www.harboroakgolf.com/scramble<br>?event=glr-festival-2022-golf-sign-up</div>
  <div class="abs price" style="left:231px;top:216px">Fees for scramble are <b>$125.</b></div>
  <div class="abs bold" style="left:232px;top:241px;font-size:6px">EMAIL</div>
  <div class="field" style="left:255px;top:236px;width:96px"></div>
  <div class="abs bold" style="left:356px;top:241px;font-size:6px">AVERAGE SCORE</div>
  <div class="field" style="left:416px;top:236px;width:63px"></div>
  <div class="abs bold" style="left:232px;top:263px;font-size:6.5px">Registration will begin</div>
  <svg class="abs" style="left:232px;top:281px" width="16" height="16" viewBox="0 0 16 16"><rect x="1" y="2.5" width="14" height="12.5" rx="1" fill="none" stroke="#2e3192" stroke-width="1.2"/><rect x="1" y="2.5" width="14" height="3" fill="#2e3192"/><rect x="4" y="0.5" width="1.4" height="3.5" fill="#2e3192"/><rect x="10.6" y="0.5" width="1.4" height="3.5" fill="#2e3192"/><circle cx="11" cy="11" r="3" fill="#fff" stroke="#2e3192"/><path d="M11 9.5V11h1.2" stroke="#2e3192" fill="none" stroke-width=".8"/></svg>
  <div class="abs bold" style="left:256px;top:281px;font-size:6.8px;line-height:1.3">Saturday, October 7th, at 7:45 AM ET, and we will<br>tee off at 8:30 AM. ET</div>
  <div class="abs small" style="left:232px;top:303px"><span class="blue-tick"></span>lunch &nbsp;&nbsp;<span class="blue-tick"></span>Beverage cart drinks &nbsp;&nbsp;<span class="blue-tick"></span>snacks are included</div>
  <div class="abs bold" style="left:232px;top:321px;font-size:6.5px">Sponsors</div>
  <div class="sponsor-box">
    <div class="sponsor-row" style="top:13px">Brightline – <b>Golf Towel</b></div>
    <div class="sponsor-row" style="top:31px;left:0;width:140px;padding:2px 8px;background:linear-gradient(90deg,#eee,#fff)">Veldtrix Corporation – <b>lunch</b></div>
    <div class="sponsor-row" style="top:53px">Northgate Design- <b>drink cart</b></div>
    <div class="partner" style="left:163px;top:18px">BRIGHTLINE</div>
    <div class="partner" style="left:170px;top:45px">VELDTRIX</div>
  </div>

  <div class="abs heading" style="left:232px;top:423px;font-size:8.5px">SPORTING CLAY</div>
  <div class="abs bold" style="left:232px;top:438px;font-size:6.3px">CEDAR HOLLOW HUNTING CLUB AND SPORTING CLAY</div>
  <svg class="abs" style="left:232px;top:456px" width="8" height="11" viewBox="0 0 9 12"><path d="M4.5 0C2 0 0 2 0 4.5 0 7.5 4.5 12 4.5 12S9 7.5 9 4.5C9 2 7 0 4.5 0z" fill="#2e3192"/><circle cx="4.5" cy="4.5" r="1.7" fill="#fff"/></svg>
  <div class="abs small" style="left:245px;top:455px;line-height:1.25">1420 Millbrook Road, Owenton, KY 40300 US<br>55 Minutes from the hotel</div>
  <div class="bar" style="left:232px;top:477px;width:247px;height:24px;justify-content:center;font-size:7.5px">www.cedarhollowhunt.com</div>
  <div class="abs price" style="left:232px;top:505px"><b>$150</b> per person <span class="small" style="margin-left:3px">Fees include food, drinks, snacks, and ammo</span></div>
  <div class="abs bold" style="left:232px;top:532px;font-size:6px">EMAIL</div>
  <div class="field" style="left:255px;top:527px;width:96px"></div>
  <div class="field" style="left:362px;top:527px;width:117px"></div>
  <div class="abs heading" style="left:232px;top:553px;font-size:8.5px">STATIC TRADE SHOW BOOTH REQUESTS</div>
  <div class="abs" style="left:232px;top:566px;font-size:10px;font-weight:500">Trade Show Booth (6 ft table) $100</div>
  <div class="abs heading" style="left:232px;top:591px;font-size:6.8px">GLR ANNUAL MEETING SPONSORS</div>
  <div class="meeting-sponsors"><span>ASHFORD</span><span>POLAR ROUTE</span><span>HARTWELL</span><span>ZENTARA</span></div>
  <div class="foot"></div>
</section>

</body>
</html>
```